Update Law Firm Website

Update law firm website pages, add pages for employees. Current website looks stale. www.vantholmlegal.example

Target Market(s)

Personal injury clients

Industry/Entity Type

Legal

Number of Pages Required

5+ page

Font styles to use
Serif

Requirements
Must have
• User friendly and engaging design
Nice to have
• ?
Should not have
• scales of justice, law books,

```html
<!DOCTYPE html>
<html lang="en">
<head>
<meta charset="utf-8">
<title>Vantholm Legal Group</title>
<link href="https://fonts.googleapis.com/css2?family=Libre+Baskerville:wght@400;700&family=Open+Sans:wght@400;600;700;800&display=swap" rel="stylesheet">
<style>
:root{
  --yellow:#fdd065;
  --gold:#f1bd52;
  --dark:#262626;
  --ink:#222;
  --muted:#666;
  --line:#d8d8d8;
  --paper:#fff;
  --card:#eeeeee;
}
*{box-sizing:border-box;margin:0;padding:0}
html,body{width:1200px;height:3180px;overflow:hidden;background:var(--paper)}
body{position:relative;font-family:"Open Sans",Arial,sans-serif;color:var(--ink)}
.abs{position:absolute}
.serif{font-family:"Libre Baskerville",Georgia,serif}
section,header,nav,footer{position:absolute;left:0;width:1200px}

/* top bar */
.topbar{top:0;height:46px;border-bottom:1px solid #e6e6e6}
.social-top{left:100px;top:14px;display:flex;gap:22px}
.social-top span{width:16px;height:16px;border-radius:50%;background:#9a9a9a;display:block}
.consult{right:78px;top:0;width:222px;height:50px;background:var(--dark);color:#fff;font-weight:700;font-size:17px;border-radius:0 0 6px 6px;display:flex;align-items:center;justify-content:center;gap:8px}
.drop-tab{left:574px;top:0;width:52px;height:28px;background:var(--gold);border-radius:0 0 26px 26px;display:flex;justify-content:center;align-items:center}

/* brand */
.brand{top:46px;height:79px;text-align:center}
.brand .name{margin-top:16px;font-size:23px;letter-spacing:1px;color:#111}
.brand .sub{font-size:12px;color:var(--gold);letter-spacing:1px;margin-top:3px}

/* nav */
.mainnav{top:125px;height:51px;background:var(--yellow);display:flex;justify-content:center;gap:30px;align-items:center;font-size:16px}
.mainnav a{color:#111;text-decoration:none}

/* hero */
.hero{top:176px;height:574px;background:linear-gradient(90deg,#5a5a5a 0%,#9a9a9a 40%,#cfcfcf 62%,#777 100%);overflow:hidden}
.hero-photo{left:0;top:0;width:1200px;height:574px}
.hero-person{right:60px;top:40px;width:280px;height:534px;background:linear-gradient(180deg,#3a3a3a,#111);border-radius:140px 140px 0 0;opacity:.85}
.hero-circle{left:76px;top:126px;width:318px;height:318px;border-radius:50%;background:rgba(60,60,60,.82);text-align:center;color:#fff}
.hero-circle .q{margin-top:64px;font-weight:700;font-size:19px;color:#111;color:#fff}
.hero-circle .big{font-weight:800;font-size:44px;line-height:48px;color:var(--yellow);margin-top:4px}
.hero-circle .small{font-size:17px;line-height:23px;margin-top:10px}
.hero-call{left:202px;top:412px;width:64px;height:64px;border-radius:50%;background:var(--yellow);display:flex;align-items:center;justify-content:center}
.phone-bar{left:78px;top:487px;width:834px;height:52px;background:var(--yellow);border-radius:8px 0 0 8px;font-size:30px;padding-left:22px;line-height:52px;color:#222}
.tab{width:62px;height:30px;border-radius:31px 31px 0 0;display:flex;align-items:flex-end;justify-content:center;padding-bottom:4px;left:569px}
.tab.y{background:var(--gold)}
.tab.w{background:#fff}

/* about */
.about{top:750px;height:525px}
.section-title{width:100%;text-align:center;font-size:38px;color:#222}
.about .section-title{top:50px}
.about-text{left:78px;top:118px;width:300px;font-size:14.5px;line-height:21px;color:#555}
.badge{left:84px;top:318px;width:250px;height:66px;background:linear-gradient(90deg,#2a2a2a,#555);border-radius:4px}
.portrait{left:524px;top:112px;width:150px;height:166px;border:2px solid #ccc;padding:6px;background:#fff}
.portrait div{width:100%;height:100%;background:linear-gradient(180deg,#7a6f66,#2b2b33)}
.lawyer-name{left:400px;width:400px;top:300px;text-align:center;font-size:25px}
.lawyer-title{left:400px;width:400px;top:340px;text-align:center;font-size:17px;color:#444;line-height:23px}
.btn-yellow{left:490px;top:420px;width:220px;height:53px;background:var(--yellow);border-radius:5px;font-size:19px;display:flex;align-items:center;justify-content:center;color:#222}
.info-card{left:822px;top:112px;width:302px;height:304px;border:2px solid #ccc;box-shadow:0 0 6px rgba(0,0,0,.15);padding:22px 26px;font-size:14.5px;line-height:21px;color:#444}
.info-card h3{font-size:19px;color:#222;margin-bottom:20px;font-weight:700}
.info-card p{margin-bottom:13px}
.info-card b{color:#222}
.info-card .ind{padding-left:50px}

/* services */
.services{top:1275px;height:480px;background:linear-gradient(180deg,#1e1e1e,#3a3a3a 50%,#1c1c1c)}
.services .section-title{top:48px;color:#fff}
.svc{top:118px;width:233px;height:303px;background:var(--card);text-align:center}
.svc .img{height:155px;background:linear-gradient(180deg,#bfc4c8,#7d8288)}
.svc .ic{position:absolute;left:90px;top:124px;width:54px;height:54px;border-radius:50%;background:#fff;display:flex;align-items:center;justify-content:center}
.svc .ic i{width:40px;height:40px;border-radius:50%;background:var(--yellow);display:flex;align-items:center;justify-content:center}
.svc h4{margin-top:40px;font-size:17px;font-weight:400}
.svc p{font-size:14px;line-height:19px;color:#777;padding:6px 22px 0}
.svc .plus{position:absolute;left:89px;bottom:0;width:56px;height:26px;background:var(--gold);border-radius:28px 28px 0 0;font-size:22px;font-weight:700;line-height:28px}

/* emergency */
.emergency{top:1755px;height:200px;background:linear-gradient(90deg,#d9a84a,#e9bd5f 50%,#d9a84a);text-align:center;color:#fff}
.emergency h2{margin-top:40px;font-size:31px;font-weight:400}
.emergency p{font-size:19px;margin-top:6px}
.btn-white{left:488px;top:118px;width:224px;height:46px;background:#fff;color:#333;border-radius:4px;font-size:18px;line-height:46px}

/* news */
.news{top:1955px;height:490px}
.news .section-title{top:48px;font-size:36px;letter-spacing:1px}
.post{top:114px;width:312px;height:330px}
.post .img{height:187px;background:linear-gradient(180deg,#c9ced3,#7d7570)}
.post .date{position:absolute;left:122px;top:152px;width:68px;height:66px;background:var(--yellow);border:3px solid #fff;border-radius:6px;text-align:center;font-size:28px;line-height:36px}
.post .date small{display:block;font-size:15px;line-height:18px}
.post .meta{position:absolute;right:4px;top:196px;font-size:11px;color:#999}
.post h5{margin-top:47px;font-size:16px;font-weight:600}
.post p{font-size:15px;line-height:21px;color:#666;margin-top:8px}

/* testimonial */
.testimonial{top:2445px;height:325px;background:linear-gradient(90deg,#3b2a1d,#1f1610 50%,#2c2016)}
.testimonial .section-title{top:50px;color:#fff;font-size:36px}
.quote-mark{left:268px;top:120px;font-size:140px;color:rgba(255,255,255,.35);font-family:Georgia,serif;line-height:1}
.avatar{left:340px;top:132px;width:104px;height:104px;border-radius:50%;border:4px solid #fff;background:linear-gradient(180deg,#8b6d58,#3b2d25)}
.quote{left:472px;top:140px;width:490px;font-size:15px;line-height:21px;color:#eee}
.dots{left:560px;top:275px;display:flex;gap:5px}
.dots span{width:15px;height:15px;border-radius:50%;border:2px solid #fff}
.dots span.on{background:var(--yellow);border-color:var(--yellow)}

/* contact */
.contact{top:2770px;height:350px}
.contact .section-title{top:55px;font-size:36px}
.col-title{font-size:19px;color:var(--gold)}
.fname{left:78px;top:102px;font-size:17px;letter-spacing:.5px}
.fsub{left:78px;top:124px;width:336px;font-size:12px;color:var(--gold);letter-spacing:1px;text-align:center}
.fabout{left:78px;top:158px;width:345px;font-size:14.5px;line-height:21px;color:#555}
.fsocial{left:78px;top:290px;display:flex;gap:12px}
.fsocial span{width:40px;height:40px;border-radius:50%;border:2px solid #666;display:block}
.fsocial span.on{background:var(--yellow);border-color:#333}
.news-col{left:472px;top:104px;width:260px}
.news-col p{font-size:15px;line-height:22px;color:#555;margin-top:10px}
.email-field{margin-top:20px;border-bottom:1px solid #aaa;padding:6px 4px;font-size:14px;color:#999;width:230px}
.btn-dark{margin-top:14px;width:156px;height:48px;background:#111;color:#fff;font-size:18px;line-height:48px;text-align:center}
.touch{left:812px;top:104px;width:330px}
.touch .row{display:flex;gap:16px;margin-top:18px;font-size:15px;line-height:22px;color:#444}
.touch svg{flex:none;margin-top:3px}

/* footer */
.footer{top:3120px;height:60px;border-top:1px solid #ccc;text-align:center;font-size:15px;line-height:58px;color:#222}
</style>
</head>
<body>

<header class="topbar">
  <div class="abs social-top" aria-label="Social links"><span></span><span></span><span></span><span></span></div>
  <div class="abs drop-tab"><svg width="18" height="12" viewBox="0 0 18 12"><path d="M2 2l7 7 7-7" stroke="#222" stroke-width="3" fill="none"/></svg></div>
  <div class="abs consult"><svg width="18" height="18" viewBox="0 0 18 18"><rect x="1" y="3" width="13" height="13" fill="none" stroke="#fff" stroke-width="2"/><path d="M5 9l3 3 8-9" stroke="#fff" stroke-width="2.4" fill="none"/></svg>Free Consultation</div>
</header>

<header class="brand">
  <div class="name serif">VANTHOLM LEGAL GROUP</div>
  <div class="sub serif">MARTIN R. VANTHOLM, ESQUIRE</div>
</header>

<nav class="mainnav">
  <a>Home</a><a>Slip and Fall</a><a>Auto Accident</a><a>Construction Injuries</a><a>Medical Malpractice</a><a>Results</a><a>About Us</a><a>Contcat Us</a>
</nav>

<section class="hero">
  <div class="abs hero-photo" role="img" aria-label="Black and white office desk with books in soft focus"></div>
  <div class="abs hero-person" role="img" aria-label="Photo of a confident lawyer in a dark suit, arms folded"></div>
  <div class="abs hero-circle">
    <div class="q">HAVING LEGAL ISSUE?</div>
    <div class="big">WE WILL<br>HELP YOU...</div>
    <div class="small">For a Free Case Evaluation,<br>contact us today</div>
  </div>
  <div class="abs hero-call"><svg width="30" height="30" viewBox="0 0 24 24"><path d="M6.6 10.8c1.4 2.8 3.8 5.1 6.6 6.6l2.2-2.2c.3-.3.7-.4 1-.2 1.1.4 2.3.6 3.6.6.6 0 1 .4 1 1V20c0 .6-.4 1-1 1C10.6 21 3 13.4 3 4c0-.6.4-1 1-1h3.5c.6 0 1 .4 1 1 0 1.3.2 2.5.6 3.6.1.3 0 .7-.2 1z" fill="#222"/></svg></div>
  <div class="abs phone-bar">(555) 014-2290</div>
  <div class="abs tab w" style="top:544px"><svg width="18" height="16" viewBox="0 0 18 16"><path d="M9 1L1 8h2.5v7h4v-5h3v5h4V8H17z" fill="#222"/></svg></div>
</section>

<section class="about">
  <div class="abs tab y" style="top:-30px"><svg width="18" height="16" viewBox="0 0 18 16"><path d="M9 1L1 8h2.5v7h4v-5h3v5h4V8H17z" fill="#222"/></svg></div>
  <h2 class="abs section-title serif">About Us</h2>
  <p class="abs about-text">Martin R. Vantholm has successfully handled death and serious personal injury cases involving automobiles and tractor trailers, injuries caused by toxic products, pipeline explosion cases, slip and fall cases involving commercial businesses, and cases against insurance companies.</p>
  <div class="abs badge" role="img" aria-label="Recognition badge"></div>
  <div class="abs portrait"><div role="img" aria-label="Portrait photo of the lead attorney"></div></div>
  <div class="abs lawyer-name serif">Mr. Martin R. Vantholm</div>
  <div class="abs lawyer-title">2006 &amp; 2007 Regional Rising Star,<br>Top Counsel</div>
  <div class="abs btn-yellow">VIEW FULL PROFILE</div>
  <div class="abs info-card">
    <h3>Mr. Martin Vantholm</h3>
    <p><b>Add :</b> 820 Alder Row #410,<br><span class="ind">Brookfield, ST 00142</span></p>
    <p><b>Contact No :</b> (555) 014-3170</p>
    <p><b>Email :</b> martin@vantholmlegal.example</p>
    <p style="margin-bottom:0"><b>Education :</b><br>&nbsp;&nbsp;&nbsp;&nbsp;Northfield State University(B.S. 1992)<br>&nbsp;&nbsp;&nbsp;&nbsp;Easton College of Law (J.D. 1995)</p>
  </div>
</section>

<section class="services">
  <div class="abs tab w" style="top:-30px"><svg width="18" height="16" viewBox="0 0 18 16"><circle cx="6" cy="9" r="4" fill="none" stroke="#222" stroke-width="2"/><circle cx="13" cy="5" r="3" fill="none" stroke="#222" stroke-width="2"/></svg></div>
  <h2 class="abs section-title serif">Our Services</h2>
  <div class="abs svc" style="left:78px"><div class="img" role="img" aria-label="Photo of a person slipping beside a wet floor sign"></div><div class="ic"><i><svg width="20" height="20" viewBox="0 0 20 20"><circle cx="10" cy="5" r="2.5" fill="#222"/><path d="M10 8l-3 6M10 8l3 5" stroke="#222" stroke-width="2"/></svg></i></div><h4 class="serif">Slip and Fall</h4><p>Lorem Ipsum is simply dummy text of the printing...</p><div class="plus">+</div></div>
  <div class="abs svc" style="left:350px"><div class="img" role="img" aria-label="Photo of a damaged car after an accident"></div><div class="ic"><i><svg width="22" height="14" viewBox="0 0 22 14"><path d="M2 9l3-6h12l3 6v3H2z" fill="#222"/></svg></i></div><h4 class="serif">Auto Accident</h4><p>Lorem Ipsum is simply dummy text of the printing...</p><div class="plus">+</div></div>
  <div class="abs svc" style="left:619px"><div class="img" role="img" aria-label="Photo of an injured construction worker being helped"></div><div class="ic"><i><svg width="20" height="20" viewBox="0 0 20 20"><path d="M4 11a6 6 0 0112 0H4zM3 12h14v2H3z" fill="#222"/></svg></i></div><h4 class="serif">Construction Injuries</h4><p>Lorem Ipsum is simply dummy text of the printing...</p><div class="plus">+</div></div>
  <div class="abs svc" style="left:888px"><div class="img" role="img" aria-label="Photo of a worried surgeon in scrubs"></div><div class="ic"><i><svg width="20" height="20" viewBox="0 0 20 20"><path d="M8 3h4v5h5v4h-5v5H8v-5H3V8h5z" fill="#222"/></svg></i></div><h4 class="serif">Medical Malpractice</h4><p>Lorem Ipsum is simply dummy text of the printing...</p><div class="plus">+</div></div>
</section>

<section class="emergency">
  <h2 class="serif">NEED EMERGENCY HELP FOR LEGAL?</h2>
  <p>We Are Waiting For Your Request</p>
  <div class="abs btn-white">GET A FREE QUOTE</div>
</section>

<section class="news">
  <div class="abs tab y" style="top:-30px"><svg width="18" height="14" viewBox="0 0 18 14"><rect x="1" y="1" width="16" height="12" fill="none" stroke="#222" stroke-width="2"/><path d="M4 5h10M4 9h7" stroke="#222" stroke-width="2"/></svg></div>
  <h2 class="abs section-title serif">LATEST NEWS</h2>
  <div class="abs post" style="left:78px"><div class="img" role="img" aria-label="Photo of a legal team standing together"></div><div class="date">30<small>Dec</small></div><div class="meta">&#9679; 05 &nbsp;&#9825; 05</div><h5>Lorem Ipsum is simply dummy text.</h5><p>Lorem Ipsum is simply dummy text of the printing and typesetting industry. Lorem Ipsum has been the industry...</p></div>
  <div class="abs post" style="left:445px"><div class="img" role="img" aria-label="Photo of a meeting in a bright office"></div><div class="date">30<small>Dec</small></div><div class="meta">&#9679; 05 &nbsp;&#9825; 05</div><h5>Lorem Ipsum is simply dummy text.</h5><p>Lorem Ipsum is simply dummy text of the printing and typesetting industry. Lorem Ipsum has been the industry...</p></div>
  <div class="abs post" style="left:812px"><div class="img" role="img" aria-label="Photo of a lawyer consulting a client at a desk"></div><div class="date">30<small>Dec.</small></div><div class="meta">&#9679; 05 &nbsp;&#9825; 05</div><h5>Lorem Ipsum is simply dummy text.</h5><p>Lorem Ipsum is simply dummy text of the printing and typesetting industry. Lorem Ipsum has been the industry...</p></div>
</section>

<section class="testimonial">
  <div class="abs tab w" style="top:-30px"><svg width="16" height="12" viewBox="0 0 16 12"><path d="M1 11V6l3-5h2L4 6h2v5zM9 11V6l3-5h2l-2 5h2v5z" fill="#222"/></svg></div>
  <h2 class="abs section-title serif">Testimonial</h2>
  <div class="abs quote-mark">&ldquo;</div>
  <div class="abs avatar" role="img" aria-label="Client portrait photo"></div>
  <p class="abs quote">"Lorem Ipsum is simply dummy text of the printing and typesetting industry. Lorem Ipsum has been the industry's standard dummy text ever since the 1500.Lorem Ipsum is simply dummy text of the printing and typesetting industry. Lorem Ipsum has been the industry."</p>
  <div class="abs dots"><span class="on"></span><span></span><span></span><span></span></div>
</section>

<section class="contact">
  <div class="abs tab y" style="top:-30px"><svg width="14" height="16" viewBox="0 0 14 16"><path d="M7 1a5 5 0 00-5 5c0 4 5 9 5 9s5-5 5-9a5 5 0 00-5-5z" fill="none" stroke="#222" stroke-width="2"/></svg></div>
  <h2 class="abs section-title serif">Contact Us</h2>
  <div class="abs fname serif">VANTHOLM LEGAL GROUP</div>
  <div class="abs fsub serif">MARTIN R. VANTHOLM, ESQUIRE</div>
  <p class="abs fabout">Martin R. Vantholm, Esquire and the Vantholm Legal Group offers legal services for when you need a Slip and Fall Lawyer, Car Accident Lawyer, Injury Lawyer, Transit Accident Lawyer, and Medical Malpractice Lawyer.</p>
  <div class="abs fsocial" aria-label="Social links"><span class="on"></span><span></span><span></span><span></span></div>
  <div class="abs news-col">
    <div class="col-title">Newsletter</div>
    <p>Lorem Ipsum is simply dummy text of the printing and typesetting.</p>
    <div class="email-field">Email id</div>
    <div class="btn-dark">SUBMIT</div>
  </div>
  <div class="abs touch">
    <div class="col-title">Get n Touch</div>
    <div class="row"><svg width="18" height="18" viewBox="0 0 18 18"><path d="M9 1v16M3 5h12M3 9h12" stroke="#f1bd52" stroke-width="2"/></svg><span>Martin R. Vantholm,<br>820 Alder Row #410,<br>Brookfield, ST 00142</span></div>
    <div class="row"><svg width="18" height="18" viewBox="0 0 24 24"><path d="M6.6 10.8c1.4 2.8 3.8 5.1 6.6 6.6l2.2-2.2c.3-.3.7-.4 1-.2 1.1.4 2.3.6 3.6.6.6 0 1 .4 1 1V20c0 .6-.4 1-1 1C10.6 21 3 13.4 3 4c0-.6.4-1 1-1h3.5c.6 0 1 .4 1 1 0 1.3.2 2.5.6 3.6.1.3 0 .7-.2 1z" fill="#f1bd52"/></svg><span>(555) 014-3170</span></div>
    <div class="row"><svg width="18" height="14" viewBox="0 0 18 14"><rect x="1" y="1" width="16" height="12" fill="none" stroke="#f1bd52" stroke-width="1.6"/><path d="M1 1l8 7 8-7" fill="none" stroke="#f1bd52" stroke-width="1.6"/></svg><span>martin@vantholmlegal.example</span></div>
  </div>
</section>

<footer class="footer">
  <div class="abs tab y" style="top:-30px"><svg width="16" height="10" viewBox="0 0 16 10"><path d="M2 8l6-6 6 6" stroke="#222" stroke-width="2.6" fill="none"/></svg></div>
  &copy; <b>VANTHOLM LEGAL GROUP</b> , Martin R. Vantholm - 2016 All Right Reserved
</footer>

</body>
</html>
```